Pebble Ledger WEB application

We need a small webdesign for a WEB-Application. Functionality will be provided by our developers. All we need are templates with HTML5, CSS and Java functionality for the "animated" parts. As well as some images and logos .
See attached Powerpoint. Please ignore last slide.
Design should be state of the art material design as know from Quorvix or Zelpad latest OS versions
In the end will be fluid design (fitting automatically to actual screen size) but template should base on 540 x 960

Target Market(s)

UK Mobile Market

Number of Pages Required

5+ page

Font styles to use
Sans Serif

Requirements
Must have
• next to requierements in Powerpoint we need animations as stated in PP (progress animation).
Nice to have
• All textfiles should be in a XML file to be easily translated to other languages.Can be done by our developers as well

```html
<!DOCTYPE html>
<html lang="en">
<head>
<meta charset="utf-8">
<title>Pebble Ledger – Battery Optimization</title>
<link rel="stylesheet" href="https://fonts.googleapis.com/css2?family=Roboto:wght@300;400;500;700&display=swap">
<style>
  :root {
    --screen-bg: #2c3843;
    --system-bar: #000000;
    --text-light: #ffffff;
    --accent: #22b8b8;
    --track: #d3d6d8;
    --system: #e24a7c;
    --memory-a: #17a596; --memory-b: #72e3d3;
    --accounts-a: #2c68d3; --accounts-b: #5ea3f2;
    --sync: #f08b25;
    --local-a: #d33c9d; --local-b: #e98ac8;
    --bluetooth-a: #1c7878; --bluetooth-b: #52c2c2;
    --apps: #2fa9e1;
    --button: #23b9b7;
  }
  * { box-sizing: border-box; margin: 0; padding: 0; }
  html, body { width: 675px; height: 1200px; overflow: hidden; }
  body { font-family: "Roboto", sans-serif; background: var(--screen-bg); color: var(--text-light); position: relative; }

  .status-bar { position: absolute; top: 0; left: 0; width: 675px; height: 47px; background: var(--system-bar); display: flex; align-items: center; justify-content: flex-end; padding-right: 40px; }
  .status-bar .wifi { margin-right: 22px; }
  .status-bar .clock { font-size: 23px; margin-right: 20px; white-space: nowrap; }
  .status-bar .level { font-size: 23px; margin-right: 18px; white-space: nowrap; }
  .status-bar .cell { display: block; }

  .app-header { position: absolute; top: 47px; left: 0; width: 675px; height: 110px; }
  .app-header .menu { position: absolute; left: 34px; top: 38px; }
  .app-header .title { position: absolute; left: 130px; top: 36px; font-size: 31px; font-weight: 400; letter-spacing: 0.5px; }

  .charge { position: absolute; left: 48px; top: 168px; font-size: 92px; font-weight: 300; color: var(--accent); line-height: 1; }
  .charge-icon { position: absolute; left: 302px; top: 180px; }
  .gain { position: absolute; left: 48px; top: 313px; font-size: 24px; color: var(--accent); letter-spacing: 0.3px; }

  .usage-list { position: absolute; left: 50px; top: 373px; width: 572px; list-style: none; }
  .usage-row { height: 80.5px; }
  .usage-label { font-size: 23px; line-height: 30px; letter-spacing: 0.3px; }
  .usage-track { margin-top: 11px; height: 10px; border-radius: 5px; background: var(--track); overflow: hidden; }
  .usage-fill { height: 100%; border-radius: 5px; }
  .fill-system { width: 19%; background: var(--system); }
  .fill-memory { width: 48%; background: linear-gradient(90deg, var(--memory-a), var(--memory-b)); }
  .fill-accounts { width: 56%; background: linear-gradient(90deg, var(--accounts-a), var(--accounts-b)); }
  .fill-sync { width: 66%; background: var(--sync); }
  .fill-local { width: 70%; background: linear-gradient(90deg, var(--local-a), var(--local-b)); }
  .fill-bluetooth { width: 90%; background: linear-gradient(90deg, var(--bluetooth-a), var(--bluetooth-b)); }
  .fill-apps { width: 83%; background: var(--apps); }

  .cta { position: absolute; left: 68px; top: 940px; width: 540px; height: 78px; border-radius: 39px; background: var(--button); color: var(--text-light); font-size: 29px; font-weight: 400; display: flex; align-items: center; justify-content: center; letter-spacing: 0.3px; }
  .cta strong { font-weight: 700; margin: 0 8px; }

  .nav-bar { position: absolute; top: 1048px; left: 0; width: 675px; height: 152px; background: var(--system-bar); }
  .nav-bar svg { position: absolute; }
  .nav-bar .back { left: 116px; top: 40px; }
  .nav-bar .home { left: 310px; top: 40px; }
  .nav-bar .recent { left: 506px; top: 44px; }
  .nav-bar .device-code { position: absolute; left: 628px; top: 98px; font-size: 22px; }
</style>
</head>
<body>
  <header class="status-bar">
    <svg class="wifi" width="36" height="26" viewBox="0 0 40 28"><path d="M20 28 L0 6 A30 30 0 0 1 40 6 Z" fill="#fff"/></svg>
    <span class="clock">12:02 AM</span>
    <span class="level">26%</span>
    <svg class="cell" width="30" height="22" viewBox="0 0 30 22"><rect x="1" y="1" width="24" height="20" rx="2" fill="none" stroke="#fff" stroke-width="2"/><rect x="26" y="7" width="3" height="8" fill="#fff"/><rect x="4" y="4" width="6" height="14" fill="#fff"/></svg>
  </header>

  <div class="app-header">
    <svg class="menu" width="50" height="34" viewBox="0 0 50 34"><rect y="0" width="50" height="5" fill="#fff"/><rect y="14" width="50" height="5" fill="#fff"/><rect y="28" width="50" height="5" fill="#fff"/></svg>
    <h1 class="title">BATTERY OPTIMIZATION</h1>
  </div>

  <div class="charge">26 %</div>
  <svg class="charge-icon" width="60" height="112" viewBox="0 0 60 112">
    <rect x="18" y="2" width="24" height="10" fill="#fff"/>
    <rect x="3" y="12" width="54" height="97" rx="4" fill="none" stroke="#fff" stroke-width="5"/>
    <rect x="11" y="63" width="38" height="14" fill="#fff"/>
    <rect x="11" y="82" width="38" height="19" fill="#fff"/>
  </svg>
  <p class="gain">INCREASE BATTERY LIFE TIME: 3H50MIN</p>

  <ul class="usage-list">
    <li class="usage-row"><div class="usage-label">SYSTEM (30 %)</div><div class="usage-track"><div class="usage-fill fill-system"></div></div></li>
    <li class="usage-row"><div class="usage-label">MEMORY (50 %)</div><div class="usage-track"><div class="usage-fill fill-memory"></div></div></li>
    <li class="usage-row"><div class="usage-label">ACCOUNTS (55 %)</div><div class="usage-track"><div class="usage-fill fill-accounts"></div></div></li>
    <li class="usage-row"><div class="usage-label">SYNC PROCESSES (60 %)</div><div class="usage-track"><div class="usage-fill fill-sync"></div></div></li>
    <li class="usage-row"><div class="usage-label">LOCALIZATION (65 %)</div><div class="usage-track"><div class="usage-fill fill-local"></div></div></li>
    <li class="usage-row"><div class="usage-label">BLUETOOTH (85 %)</div><div class="usage-track"><div class="usage-fill fill-bluetooth"></div></div></li>
    <li class="usage-row"><div class="usage-label">APPS (80 %)</div><div class="usage-track"><div class="usage-fill fill-apps"></div></div></li>
  </ul>

  <div class="cta">START <strong>FREE</strong> OPTIMIZATION NOW</div>

  <nav class="nav-bar">
    <svg class="back" width="50" height="56" viewBox="0 0 50 56"><path d="M46 4 L4 28 L46 52 Z" fill="none" stroke="#fff" stroke-width="4" stroke-linejoin="round"/></svg>
    <svg class="home" width="56" height="56" viewBox="0 0 56 56"><circle cx="28" cy="28" r="25" fill="none" stroke="#fff" stroke-width="4"/></svg>
    <svg class="recent" width="48" height="48" viewBox="0 0 48 48"><rect x="2" y="2" width="44" height="44" rx="2" fill="none" stroke="#fff" stroke-width="4"/></svg>
    <span class="device-code">C14</span>
  </nav>
</body>
</html>
```